Gourmet Restaurant take out menu

We need a take out menu design that is trendy for a casual upscale Italian restaurant with a vast menu. This menu must be able to be 4 color and reproducible in large quantities to be bulked mailed or inserted into a daily paper. It must also maintain a theme that can be crossed over to our in house dining menu and specials menu.
OUR WEBSITE:
www.bellavistoplates.example
For the content, go to the Menu section of our website. We are interested in the design scheme and a template to use.
Target Market(s)
families, sinle individuals seeking take out meals and delivery
Industry/Entity Type
Restaurant
Look and feel
Each slider illustrates characteristics of the customer's brand and the style your logo design should communicate.

```html
<!DOCTYPE html>
<html lang="en">
<head>
<meta charset="utf-8">
<title>Bella Visto Plates – Take Out Menu</title>
<link href="https://fonts.googleapis.com/css2?family=Open+Sans:wght@400;600&family=Lobster+Two:ital,wght@1,700&family=Cormorant+SC:wght@500;600&family=Alfa+Slab+One&family=Oswald:wght@300&display=swap" rel="stylesheet">
<style>
:root{
  --orange:#f28c1e;
  --orange-light:#f6a94e;
  --text:#3a3a3a;
  --brown:#8e2a12;
  --paper:#ffffff;
}
*{margin:0;padding:0;box-sizing:border-box}
html,body{width:1200px;height:774px;overflow:hidden;background:var(--paper)}
body{font-family:"Open Sans",sans-serif;color:var(--text);font-size:9.4px;line-height:1.3}
.menu{position:relative;width:1200px;height:774px;overflow:hidden}
.frame{position:absolute;inset:0}
.col{position:absolute;top:0;height:774px}
.col-left{left:32px;width:358px}
.col-mid{left:428px;width:352px}
.col-right{left:812px;width:358px}
.section-title{position:absolute;left:0;right:0;display:flex;align-items:center;gap:12px;font-family:"Lobster Two",cursive;font-style:italic;font-weight:700;color:var(--orange);font-size:22px;line-height:1}
.section-title::before,.section-title::after{content:"";flex:1;height:2px;background:var(--orange-light);border-radius:2px}
.note{position:absolute;left:0;right:0;text-align:center;font-size:9.4px}
.list{position:absolute;list-style:none}
.list li{height:13.2px;white-space:nowrap}
.dish{position:absolute;left:0;right:0}
.dish .name{color:var(--orange);text-transform:uppercase;font-size:9px;display:block}
.dish .desc{display:block;font-size:9px}
.burger-badge{position:absolute;left:204px;top:382px;width:150px;text-align:center;color:var(--orange);line-height:1}
.burger-badge .oz{font-family:"Alfa Slab One",serif;font-size:26px}
.burger-badge .big{font-family:"Alfa Slab One",serif;font-size:13px;letter-spacing:.5px;margin-top:3px}
.burger-badge .script{font-family:"Lobster Two",cursive;font-style:italic;font-weight:700;font-size:13px;margin-top:2px}
.burger-badge .fries{font-family:"Oswald",sans-serif;font-weight:300;font-size:24px;margin-top:2px;white-space:nowrap}
.pizza-badge{position:absolute;left:208px;top:122px;width:140px;height:140px;border-radius:50%;background:var(--orange);border:3px solid #fff;box-shadow:0 0 0 2px var(--orange);color:#fff;font-family:"Alfa Slab One",serif;text-align:center;font-size:11.5px;line-height:1.15;padding-top:20px}
.pizza-badge .slice{margin-top:10px}
.photo-frame{position:absolute;left:2px;top:48px;width:354px;height:282px;border:2px solid var(--orange-light)}
.photo{position:absolute;left:10px;top:10px;width:330px;height:260px;background:radial-gradient(circle at 55% 45%,#d8a04a 0%,#a4571f 45%,#4a2a17 100%)}
.brand{position:absolute;left:0;right:0;top:392px;text-align:center;color:var(--brown);font-family:"Cormorant SC",serif;font-weight:500}
.brand .name{font-size:40px;line-height:1;white-space:nowrap}
.brand .sub{font-size:21px;letter-spacing:2px;margin-top:10px}
.contact{position:absolute;left:0;right:0;text-align:center;color:var(--brown);font-family:"Cormorant SC",serif;font-weight:500}
.contact .label{font-weight:600;font-size:16px;line-height:1.1}
.contact .value{font-size:17px;line-height:1.2}
.hours-title{position:absolute;left:50px;right:50px;top:618px;display:flex;align-items:center;gap:10px;color:var(--brown);font-family:"Cormorant SC",serif;font-weight:600;font-size:16px}
.hours-title::before,.hours-title::after{content:"";flex:1;height:2px;background:var(--brown)}
.hours{position:absolute;left:0;right:0;text-align:center;color:var(--brown);font-family:"Cormorant SC",serif;font-weight:500;font-size:16px;line-height:1.05}
</style>
</head>
<body>
<div class="menu">
  <svg class="frame" width="1200" height="774" viewBox="0 0 1200 774">
    <g fill="none" stroke="#f6a94e" stroke-width="1.5">
      <line x1="90" y1="12" x2="1110" y2="12"/>
      <line x1="90" y1="762" x2="1110" y2="762"/>
      <line x1="12" y1="90" x2="12" y2="684"/>
      <line x1="1188" y1="90" x2="1188" y2="684"/>
      <line x1="406" y1="34" x2="406" y2="736" stroke-dasharray="2 3"/>
      <line x1="794" y1="34" x2="794" y2="736" stroke-dasharray="2 3"/>
    </g>
    <g fill="#f28c1e">
      <path d="M406 26l4 4-4 4-4-4z"/><path d="M406 732l4 4-4 4-4-4z"/>
      <path d="M794 26l4 4-4 4-4-4z"/><path d="M794 732l4 4-4 4-4-4z"/>
      <path d="M12 8l5 5-5 5-5-5z"/><path d="M1188 8l5 5-5 5-5-5z"/>
      <path d="M12 756l5 5-5 5-5-5z"/><path d="M1188 756l5 5-5 5-5-5z"/>
    </g>
  </svg>

  <section class="col col-left">
    <h2 class="section-title" style="top:43px">Hot Subs</h2>
    <p class="note" style="top:73px">add cheese for 0.59</p>
    <ul class="list" style="left:10px;top:88px">
      <li>Cheesesteak ...6.59</li><li>Bacon Cheesesteak ... 7.59</li><li>Steak Sub ... 6.29</li><li>Chicken Parmigiana ... 6.99</li><li>Pepper, Egg, &amp; Cheese ... 6.29</li><li>Pizza Cheesesteak ... 6.99</li><li>Meatball Parmigiana ... 6.99</li><li>Mushroom Cheesesteak ... 6.99</li><li>Veal Parmigiana ... 7.99</li><li>Pepper Cheesesteak ... 6.99</li>
    </ul>
    <ul class="list" style="left:191px;top:88px">
      <li>Vegetarian with Cheese ... 6.59</li><li>Eggplant Parmigiana ... 6.59</li><li>Chicken Cheesesteak ... 6.99</li><li>Sausage Parmigiana ... 7.59</li><li>Grilled Chicken ... 6.59</li><li>Cheeseburger Sub ... 7.59</li><li>Chicken Cacciatore ... 7.59</li><li>Steak Cacciatore ... 7.59</li><li>Sausage, Peppers, &amp; Onion ... 6.99</li>
    </ul>

    <h2 class="section-title" style="top:237px">Cold Subs</h2>
    <p class="note" style="top:268px">add cheese for 0.59</p>
    <ul class="list" style="left:10px;top:283px">
      <li>Regular Italian ... 6.59</li><li>Tuna ... 6.59</li><li>Roast Beef ... 7.59</li><li>Imported Ham ... 6.59</li>
    </ul>
    <ul class="list" style="left:191px;top:286px">
      <li>Roast Turkey ... 6.99</li><li>Provolone ... 6.59</li><li>Capicola, Salami, &amp; Provolone ... 6.99</li><li>Chicken Salad ... 6.99</li>
    </ul>

    <h2 class="section-title" style="top:354px">Awesome burgers</h2>
    <div class="dish" style="left:10px;top:387px"><span class="name">Cheeseburger ... 7.99</span></div>
    <div class="dish" style="left:10px;top:411px"><span class="name">Bacon Cheddar ... 8.99</span><span class="desc">Applewood smoked bacon, sharp cheddar</span></div>
    <div class="dish" style="left:10px;top:447px;right:170px"><span class="name">Blue Cheese BLT ... 9.59</span><span class="desc">Bacon, lettuce, tomato, onion, mayonnaise, bleu cheese</span></div>
    <div class="dish" style="left:10px;top:496px;right:170px"><span class="name">Portabella .. 8.59</span><span class="desc">Angus burger, roasted portabella, melted provolone cheese</span></div>
    <div class="dish" style="left:10px;top:545px"><span class="name">Gourmet Sliders... 8.99</span><span class="desc">5 bite-sized burgers with American cheese on mini potato rolls</span></div>
    <div class="dish" style="left:10px;top:582px"><span class="name">Mushroom Swiss ... 8.59</span><span class="desc">Sautéed mushrooms, onions and mayo topped with Swiss cheese</span></div>
    <div class="dish" style="left:10px;top:618px"><span class="name">California... 9.99</span><span class="desc">Avocado, roasted green chilies, pepper jack cheese, chipotle mayo, ranch dressing</span></div>
    <div class="dish" style="left:10px;top:655px"><span class="name">Pub ... 9.99</span><span class="desc">Harbor steak sauce and mayo, topped with onion rings, bleu cheese</span></div>
    <div class="dish" style="left:10px;top:691px;right:60px"><span class="name">Smokehouse Barbecue ... 9.99</span><span class="desc">Smoked bacon, melted cheddar cheese, crispy onion strings, tangy barbecue-ranch sauce</span></div>

    <div class="burger-badge">
      <div class="oz">8OZ</div>
      <div class="big">PREMIUM</div>
      <div class="big">BLACK ANGUS BEEF</div>
      <div class="script">served on a</div>
      <div class="big">KAISER ROLL</div>
      <div class="script">with</div>
      <div class="fries">FRENCH FRIES</div>
      <div class="script">and a FRIED PICKLE</div>
    </div>
  </section>

  <section class="col col-mid">
    <h2 class="section-title" style="top:43px">Gourmet Pizza</h2>
    <p style="position:absolute;top:70px;color:var(--orange)">TOPPINGS FOR 1.99</p>
    <ul class="list" style="left:0;top:94px;line-height:12px">
      <li style="height:12px">HAM • BROCCOLI • EXTRA CHEESE • TOMATOES</li>
      <li style="height:12px">HOT OR SWEET PEPPERS • ROASTED PEPPERS •</li>
      <li style="height:12px">PEPPERONI • SPINACH •</li>
      <li style="height:12px">ITALIAN SAUSAGE • BLACK OLIVES •</li>
      <li style="height:12px">GREEN PEPPERS • ONIONS</li>
      <li style="height:12px">MUSHROOMS • ANCHOVIES •</li>
      <li style="height:12px">GRILLED CHICKEN</li>
    </ul>
    <p style="position:absolute;top:191px">MEATBALL BACON and RICOTTA 3.00</p>

    <div class="pizza-badge">10" INDIVIDUAL<br>12" MEDIUM<br>16" LARGE<div class="slice">PIZZA BY THE SLICE<br>Plain 1.99,<br>Veggie</div></div>

    <div class="dish" style="top:221px"><span class="name">Plain Cheese .... 8.99/11.99/12.99</span></div>
    <div class="dish" style="top:245px"><span class="name">Traditional White .... 8.59/11.59/13.99</span><span class="desc">Olive oil, garlic, mozzarella cheese</span></div>
    <div class="dish" style="top:282px;right:150px"><span class="name">Chicken Bacon Ranch ...10.99/14.99/16.99</span><span class="desc">Garlic chicken, bacon, pepperjack and cheddar cheese, red onions, diced tomatoes, drizzle of ranch dressing</span></div>
    <div class="dish" style="top:343px"><span class="name">Bronx Bomber ... 11.99/14.99/16.99</span><span class="desc">Sausage, prosciutto ham, oregano, crumbled bleu and mozzarella cheese</span></div>
    <div class="dish" style="top:379px"><span class="name">Buffalo Chicken ... 10.99/14.99/16.99</span><span class="desc">Buffalo sauce, chicken, mozzarella cheese, side of bleu cheese dressing</span></div>
    <div class="dish" style="top:416px"><span class="name">Gourmet Special ... 12.99/16.99/18.99</span><span class="desc">Pepperoni, sausage, bell peppers, mushrooms, onion, mozzarella cheese</span></div>
    <div class="dish" style="top:452px"><span class="name">Margarita ... 8.99/11.99/13.99</span><span class="desc">Fresh basil, tomato, buffalo mozzarella cheese</span></div>
    <div class="dish" style="top:489px"><span class="name">Roasted Vegetable ... 11.99/14.99/16.99</span><span class="desc">Eggplant, red and yellow peppers, onions, artichokes, Kalamata olives, tomatoes, mozzarella cheese. Veggie Lover Olive oil, garlic, broccoli, spinach, tomato, mozzarella cheese.</span></div>
    <div class="dish" style="top:550px"><span class="name">Sweet Hawaiian ... 11.99/14.99/16.99</span><span class="desc">Pineapple, tomatoes, ham, mozzarella cheese.</span></div>
    <div class="dish" style="top:587px"><span class="name">Spinach and Artichoke ... 8.99/11.99/12.99</span><span class="desc">Spinach, artichoke hearts, basil, mozzarella, parmesan cheese.</span></div>
    <div class="dish" style="top:623px"><span class="name">Philly Cheese Steak ... 11.99/14.99/16.99</span><span class="desc">Philly steak, green peppers, onions, provolone, American cheese.</span></div>
    <div class="dish" style="top:660px"><span class="name">Grandma's Pie ... 14.99</span><span class="desc">Thin crust pizza topped with mozzarella, tomato sauce, buffalo mozzarella, fresh basil, olive oil. (One Size)</span></div>
  </section>

  <section class="col col-right">
    <div class="photo-frame"><div class="photo" role="img" aria-label="Close-up photo of a pizza slice with pepperoni, black olives and melted cheese"></div></div>
    <div class="brand"><div class="name">Bella Visto Plates</div><div class="sub">Italian Cuisine</div></div>
    <div class="contact" style="top:507px"><div class="label">Call us at</div><div class="value">555-014-2273</div></div>
    <div class="contact" style="top:556px"><div class="label">Visit us at</div><div class="value">118 W. Harbor Lane, Seaview, NJ</div></div>
    <div class="hours-title">Hours:</div>
    <p class="hours" style="top:653px">Dining Room: Mon-Thu 11am – 11pm,<br>Fri-Sat 11am – 12am, Sun 12pm – 11pm</p>
    <p class="hours" style="top:696px">Takeout: Mon-Thu 11am – 10pm, Fri-Sat<br>11am – 11pm, Sun 12pm – 10pm</p>
  </section>
</div>
</body>
</html>
```